lantern institute of business and technology web site

I need web site for the institute which focus on business courses and computer course it is also for vocation train for employment It is also carear development and advancement .It should have links to online study resource which free
Industry/Entity Type
Business
Number of Pages Required
1 page
Look and feel

```html
<!DOCTYPE html>
<html lang="en">
<head>
<meta charset="utf-8">
<title>Lantern Institute of Business and Technology</title>
<link href="https://fonts.googleapis.com/css2?family=Open+Sans:wght@400;600;700&family=Roboto:wght@400;500;700;900&display=swap" rel="stylesheet">
<style>
:root{
  --navy:#14275e;
  --navy-deep:#0f1d47;
  --blue:#1f4fa0;
  --blue-bright:#2a6fd1;
  --orange:#f2691c;
  --green:#78b23a;
  --mist:#dfe5ee;
  --ink:#333a45;
  --muted:#6b7380;
  --line:#d4d9e1;
  --white:#ffffff;
}
*{margin:0;padding:0;box-sizing:border-box}
html,body{width:1200px;height:3324px;overflow:hidden}
body{font-family:"Open Sans",Arial,sans-serif;color:var(--ink);background:var(--white);font-size:14px}
h1,h2,h3,h4{font-family:"Roboto",Arial,sans-serif}

/* Header */
.site-header{height:120px;display:flex;align-items:center;padding:0 70px;background:var(--white)}
.brand{display:flex;align-items:center;gap:14px}
.brand-mark{width:44px;height:44px;background:var(--blue)}
.brand-name{font-family:"Roboto",sans-serif;font-weight:900;font-size:40px;color:var(--navy);letter-spacing:1px}
.main-nav{margin-left:auto;display:flex;gap:28px;font-size:13px;font-weight:600}
.main-nav a{color:var(--ink);text-decoration:none}
.main-nav a.active{color:var(--orange)}
.phone-pill{margin-left:150px;background:var(--orange);color:var(--white);font-weight:700;font-size:15px;padding:10px 20px;border-radius:20px;display:flex;align-items:center;gap:8px}

/* Hero */
.hero{position:relative;height:620px;overflow:hidden}
.hero-photo{position:absolute;inset:0;background:radial-gradient(ellipse at 50% 60%,#2f5fb6 0%,#183a86 45%,#0d1f55 100%)}
.hero-copy{position:relative;text-align:center;padding-top:38px;color:var(--white)}
.hero-copy h1{font-size:46px;font-weight:500;letter-spacing:1px}
.hero-copy p{font-family:"Roboto",sans-serif;font-weight:700;font-size:20px;margin-top:6px;letter-spacing:.5px}
.hero-btn{position:absolute;left:50%;top:436px;transform:translateX(-50%);background:var(--blue-bright);color:var(--white);font-weight:700;font-size:15px;padding:13px 24px;border-radius:2px}
.hero-dots{position:absolute;left:50%;top:522px;transform:translateX(-50%);display:flex;gap:6px}
.hero-dots span{width:11px;height:11px;border-radius:50%;background:rgba(255,255,255,.45)}
.hero-dots span.on{background:var(--white)}

/* About */
.about{height:200px;padding:20px 80px 0;text-align:center}
.section-title{font-family:"Roboto",sans-serif;font-weight:700;font-size:26px;color:var(--navy-deep)}
.about .section-title{font-size:24px;padding-bottom:10px;border-bottom:1px solid var(--line);margin:0 120px 12px}
.about p{font-size:13px;line-height:1.6;color:var(--muted)}

/* Programs */
.programs{height:840px;background:var(--mist);padding-top:40px}
.programs-head{text-align:center;margin-bottom:36px}
.programs-head small{display:block;font-family:"Roboto",sans-serif;font-size:26px;font-weight:500;color:var(--navy-deep)}
.programs-head h2{font-size:48px;font-weight:700;color:var(--navy-deep);line-height:1}
.programs-head h2 .rule{display:inline-block;width:70px;height:2px;background:var(--navy-deep);vertical-align:middle;margin:0 14px}
.program-grid{display:grid;grid-template-columns:repeat(3,260px);gap:36px;justify-content:center}
.program-card{background:var(--white);height:272px;padding:22px;text-align:center;box-shadow:0 2px 4px rgba(0,0,0,.08)}
.program-icon{width:60px;height:60px;margin:0 auto 12px;border-radius:50%;background:#e8eef8;display:flex;align-items:center;justify-content:center}
.program-card h3{font-size:15px;color:var(--blue);font-weight:700;line-height:1.3;min-height:40px}
.program-card p{font-size:12.5px;color:var(--muted);line-height:1.55;margin-top:12px}
.program-card .more{display:block;margin-top:14px;font-size:11px;font-weight:700;color:var(--blue)}

/* Testimonials */
.testimonials{height:460px;padding:36px 70px 0}
.testimonials .section-title{text-align:center;font-size:24px;margin-bottom:28px}
.quote-row{display:grid;grid-template-columns:repeat(4,1fr);gap:30px}
.quote{position:relative;padding:0 30px 0 28px;font-size:12.5px;line-height:1.6;color:var(--muted);height:200px}
.quote::before{content:"\201C";position:absolute;left:0;top:-8px;font-size:40px;color:var(--ink);font-family:Georgia,serif}
.quote::after{content:"\201D";position:absolute;right:0;bottom:-10px;font-size:40px;color:var(--ink);font-family:Georgia,serif}
.quote-people{display:flex;justify-content:space-around;margin-top:24px;padding:0 40px}
.person{display:flex;align-items:center;gap:12px;font-size:12px}
.avatar{width:48px;height:48px;border-radius:50%;background:linear-gradient(135deg,#c9a98c,#7d6a5c)}
.person b{display:block;color:var(--blue);font-weight:600}
.person span{color:var(--muted)}

/* Online study */
.study-banner{position:relative;height:360px}
.study-photo{position:absolute;inset:0;background:linear-gradient(180deg,#a9c9e8 0%,#dbe9f5 55%,#c7d1da 100%)}
.study-copy{position:absolute;left:240px;top:40px}
.study-tag{background:var(--green);color:var(--white);font-family:"Roboto",sans-serif;font-weight:900;padding:10px 22px;line-height:1.05}
.study-tag .big{font-size:50px;display:block}
.study-tag .small{font-size:25px;display:block}
.study-btn{display:inline-block;margin-top:22px;margin-left:24px;background:var(--orange);color:var(--white);font-weight:700;font-size:20px;padding:14px 34px}

/* Video + highlights */
.media-block{height:380px;display:flex;gap:60px;padding:50px 70px 0}
.video-frame{position:relative;width:460px;height:280px;background:linear-gradient(135deg,#8c99a8,#cfd7df 60%,#e8ecef);box-shadow:0 2px 6px rgba(0,0,0,.15)}
.play{position:absolute;left:50%;top:50%;transform:translate(-50%,-50%)}
.highlights{list-style:none;padding-top:12px}
.highlights li{display:flex;align-items:center;gap:16px;font-family:"Roboto",sans-serif;font-size:22px;font-weight:500;color:var(--navy-deep);margin-bottom:18px}
.tick{width:30px;height:30px;background:var(--blue);display:flex;align-items:center;justify-content:center;flex:none}

/* Footer */
.signup{height:100px;background:var(--navy);display:flex;align-items:center;padding:0 70px;gap:24px}
.signup label{font-family:"Roboto",sans-serif;font-size:24px;color:var(--white)}
.signup .field{width:340px;height:36px;background:var(--white);font-size:12px;color:#9aa1ab;padding:10px 12px}
.signup .btn{background:var(--orange);color:var(--white);font-weight:700;font-size:12px;padding:11px 22px}
.site-footer{height:200px;background:var(--navy-deep);display:grid;grid-template-columns:140px 250px 260px 150px 1fr;gap:20px;padding:22px 70px 0;color:#aab4cc;font-size:11.5px;line-height:1.6}
.site-footer h4{font-size:12px;color:var(--white);font-weight:700;margin-bottom:6px;text-transform:uppercase}
.socials{display:flex;gap:8px}
.socials span{width:26px;height:26px;border-radius:50%;border:1px solid #aab4cc}
.partner-badge{width:150px;height:70px;background:#0b0b0b;margin-top:8px}
.copyright{height:44px;background:#0b1638;color:#8f99b3;font-size:11px;padding:14px 70px 0}
</style>
</head>
<body>

<header class="site-header">
  <div class="brand"><span class="brand-mark"></span><span class="brand-name">LANTERN</span></div>
  <nav class="main-nav">
    <a class="active" href="#">HOME</a><a href="#">ABOUT US</a><a href="#">COURSES</a><a href="#">CONTACT US</a>
  </nav>
  <div class="phone-pill">
    <svg width="13" height="13" viewBox="0 0 24 24"><path fill="#fff" d="M6.6 10.8a15 15 0 0 0 6.6 6.6l2.2-2.2c.3-.3.7-.4 1-.2 1.1.4 2.3.6 3.6.6.6 0 1 .4 1 1V20c0 .6-.4 1-1 1A17 17 0 0 1 3 4c0-.6.4-1 1-1h3.5c.6 0 1 .4 1 1 0 1.3.2 2.5.6 3.6.1.3 0 .7-.2 1z"/></svg>
    +260 211 555 014
  </div>
</header>

<section class="hero">
  <div class="hero-photo" role="img" aria-label="Desk workspace with desktop computer, lamp and office items on a deep blue background"></div>
  <div class="hero-copy">
    <h1>LOREM IPSUM DOLOR SIT AMET</h1>
    <p>LOREM IPSUM DOLOR SIT AMET, CONSECTETUR ADIPISCING ELIT, SED DO EIUSMOD TEMPOR.</p>
  </div>
  <span class="hero-btn">LEARN MORE</span>
  <div class="hero-dots"><span class="on"></span><span></span><span></span><span></span><span></span></div>
</section>

<section class="about">
  <h2 class="section-title">ABOUT LANTERN INSTITUTE OF BUSINESS AND TECHNOLOGY</h2>
  <p>Lantern Institute of Business and Technology is a fast growing Education and Training Solution Provider, focusing on holistic knowledge and skills interventions that impact livelihoods. It is established on the core values of making a meaningful and measurable difference on career aspirations and goals through innovative learning and knowledge management interventions. Our programs cultivate not only the professional careers but also inculcate the importance of discipline and equip them physically, mentally, socially and spiritually. The institution is licensed and registered under the Northgate Skills Council.</p>
</section>

<section class="programs">
  <div class="programs-head">
    <small>OUR PROGRAMS</small>
    <h2><span class="rule"></span>OFFERED<span class="rule"></span></h2>
  </div>
  <div class="program-grid">
    <article class="program-card">
      <div class="program-icon"><svg width="30" height="30" viewBox="0 0 24 24"><path fill="#1f4fa0" d="M12 3 1 9l11 6 9-4.9V17h2V9z"/><path fill="#1f4fa0" d="M5 13.2v4L12 21l7-3.8v-4L12 17z"/></svg></div>
      <h3>University Education – Long Distance Learning</h3>
      <p>Lorem ipsum dolor sit amet, consectetur adipiscing elit, sed do eiusmod tempor aliqua.</p>
      <span class="more">FIND OUT MORE &gt;</span>
    </article>
    <article class="program-card">
      <div class="program-icon"><svg width="30" height="30" viewBox="0 0 24 24"><rect x="3" y="4" width="18" height="12" rx="1" fill="#1f4fa0"/><rect x="8" y="18" width="8" height="2" fill="#1f4fa0"/></svg></div>
      <h3>Modular<br>Soft Skills</h3>
      <p>Lorem ipsum dolor sit amet, consectetur adipiscing elit, sed do eiusmod tempor aliqua.</p>
      <span class="more">FIND OUT MORE &gt;</span>
    </article>
    <article class="program-card">
      <div class="program-icon"><svg width="30" height="30" viewBox="0 0 24 24"><rect x="3" y="5" width="18" height="11" fill="#1f4fa0"/><circle cx="12" cy="19" r="2" fill="#1f4fa0"/></svg></div>
      <h3>Direct to Device (D2D)</h3>
      <p>Lorem ipsum dolor sit amet, consectetur adipiscing elit, sed do eiusmod tempor aliqua.</p>
      <span class="more">FIND OUT MORE &gt;</span>
    </article>
    <article class="program-card">
      <div class="program-icon"><svg width="30" height="30" viewBox="0 0 24 24"><path fill="#1f4fa0" d="M12 2a7 7 0 0 0-4 12.7V17h8v-2.3A7 7 0 0 0 12 2z"/><rect x="9" y="18" width="6" height="3" fill="#1f4fa0"/></svg></div>
      <h3>Brightpath</h3>
      <p>Lorem ipsum dolor sit amet, consectetur adipiscing elit, sed do eiusmod tempor aliqua.</p>
      <span class="more">FIND OUT MORE &gt;</span>
    </article>
    <article class="program-card">
      <div class="program-icon"><svg width="30" height="30" viewBox="0 0 24 24"><circle cx="12" cy="8" r="4" fill="#1f4fa0"/><path fill="#1f4fa0" d="M4 21c0-4.4 3.6-7 8-7s8 2.6 8 7z"/></svg></div>
      <h3>Career Roles in<br>The Talent Continuum</h3>
      <p>Lorem ipsum dolor sit amet, consectetur adipiscing elit, sed do eiusmod tempor aliqua.</p>
      <span class="more">FIND OUT MORE &gt;</span>
    </article>
    <article class="program-card">
      <div class="program-icon"><svg width="30" height="30" viewBox="0 0 24 24"><rect x="3" y="7" width="18" height="13" rx="1" fill="#1f4fa0"/><rect x="9" y="4" width="6" height="3" fill="none" stroke="#1f4fa0" stroke-width="2"/></svg></div>
      <h3>Business Verticals</h3>
      <p>Lorem ipsum dolor sit amet, consectetur adipiscing elit, sed do eiusmod tempor aliqua.</p>
      <span class="more">FIND OUT MORE &gt;</span>
    </article>
  </div>
</section>

<section class="testimonials">
  <h2 class="section-title">WHAT OTHER SAYS TESTIMONIALS</h2>
  <div class="quote-row">
    <blockquote class="quote">Lorem ipsum dolor sit amet, consectetur adipiscing elit, sed do eiusmod tempor incididunt ut labore et dolore magna aliqua. Ut enim ad minim veniam, quis nostrud exercitation ullamco laboris nisi ut aliquip ex ea commodo consequat. Duis aute irure dolor.</blockquote>
    <blockquote class="quote">Lorem ipsum dolor sit amet, consectetur adipiscing elit, sed do eiusmod tempor incididunt ut labore et dolore magna aliqua. Ut enim ad minim veniam, quis nostrud exercitation ullamco laboris nisi ut aliquip ex ea commodo consequat. Duis aute irure dolor.</blockquote>
    <blockquote class="quote">Lorem ipsum dolor sit amet, consectetur adipiscing elit, sed do eiusmod tempor incididunt ut labore et dolore magna aliqua. Ut enim ad minim veniam, quis nostrud exercitation ullamco laboris nisi ut aliquip ex ea commodo consequat. Duis aute irure dolor.</blockquote>
    <blockquote class="quote">Lorem ipsum dolor sit amet, consectetur adipiscing elit, sed do eiusmod tempor incididunt ut labore et dolore magna aliqua. Ut enim ad minim veniam, quis nostrud exercitation ullamco laboris nisi ut aliquip ex ea commodo consequat. Duis aute irure dolor.</blockquote>
  </div>
  <div class="quote-people">
    <div class="person"><div class="avatar" role="img" aria-label="Portrait of a student"></div><div><b>Chanda Phiri</b><span>Lorem ipsum</span></div></div>
    <div class="person"><div class="avatar" role="img" aria-label="Portrait of a student"></div><div><b>Mutale Banda</b><span>Lorem ipsum</span></div></div>
    <div class="person"><div class="avatar" role="img" aria-label="Portrait of a student"></div><div><b>Natasha Mwansa</b><span>Lorem ipsum</span></div></div>
  </div>
</section>

<section class="study-banner">
  <div class="study-photo" role="img" aria-label="Young woman sitting on a stack of books with a laptop against a pale sky"></div>
  <div class="study-copy">
    <div class="study-tag"><span class="big">ONLINE STUDY</span><span class="small">RESOURCE WHICH FREE</span></div>
    <span class="study-btn">GET START</span>
  </div>
</section>

<section class="media-block">
  <div class="video-frame" role="img" aria-label="Video still of a person working on a laptop at a bright desk">
    <svg class="play" width="80" height="80" viewBox="0 0 80 80"><circle cx="40" cy="40" r="38" fill="rgba(0,0,0,.35)" stroke="#fff" stroke-width="3"/><path d="M32 24v32l26-16z" fill="#fff"/></svg>
  </div>
  <ul class="highlights">
    <li><span class="tick"><svg width="16" height="16" viewBox="0 0 24 24"><path d="M4 12l5 5L20 6" fill="none" stroke="#fff" stroke-width="3"/></svg></span>Lorem ipsum dolor sit amet</li>
    <li><span class="tick"><svg width="16" height="16" viewBox="0 0 24 24"><path d="M4 12l5 5L20 6" fill="none" stroke="#fff" stroke-width="3"/></svg></span>Sed ut perspiciatis unde omnis iste</li>
    <li><span class="tick"><svg width="16" height="16" viewBox="0 0 24 24"><path d="M4 12l5 5L20 6" fill="none" stroke="#fff" stroke-width="3"/></svg></span>Qui dolorem ipsum quia dolor sit amet</li>
    <li><span class="tick"><svg width="16" height="16" viewBox="0 0 24 24"><path d="M4 12l5 5L20 6" fill="none" stroke="#fff" stroke-width="3"/></svg></span>Vel illum qui dolorem eum fugiat quo</li>
    <li><span class="tick"><svg width="16" height="16" viewBox="0 0 24 24"><path d="M4 12l5 5L20 6" fill="none" stroke="#fff" stroke-width="3"/></svg></span>Nemo enim ipsam voluptatem quia</li>
  </ul>
</section>

<section class="signup">
  <label>Join our email list</label>
  <span class="field">Enter your email address</span>
  <span class="btn">SIGN UP NOW</span>
</section>

<footer class="site-footer">
  <div><h4>Information</h4>Home<br>About Us<br>Courses<br>Contact Us</div>
  <div><h4>Programs Offered</h4>University Education – Long Distance Learning<br>Modular Soft Skills<br>Direct To Device (D2D)<br>Brightpath<br>Career Roles In The Talent Continuum<br>Business Verticals</div>
  <div><h4>Contact Info</h4>12 Kafue Road, Woodlands<br>Lusaka, Zambia<br><br>P: +260 211 555 014<br>E: info@lanterninstitute.edu</div>
  <div><h4>Follow Us</h4><div class="socials"><span></span><span></span></div></div>
  <div><h4>In Conjunction<br>With Brightpath</h4><div class="partner-badge" role="img" aria-label="Partner badge"></div></div>
</footer>
<div class="copyright">© 2015 Lantern Institute Of Business And Technology. All Rights Reserved.</div>

</body>
</html>
```